Local Directory Ad

We currently have an advertisement in our local directory (see attached). We would like to make it look more appealing.
Dimensions are 110mm H X 175mm W
We would like to keep the same colours and contact details remain the same.
Most of the content can remain the same, Just remove the line Tax effective remote area salary packaging and add in Self Managed Super Funds.We want to change mortgage broking to Mortgage Broking and Loan Structuring.

We want to change the line Local accountants Local Knowledge Local Experience - to something like Coastal Insight Second to None or unsurpassed local knowledge but open to suggestions on this.

there are some good designs posted so far. I particulalry like the ones from pulmawick, korbu41, and the last one posted by wexlorunti and PLV. Keep up the good work guys

```html
<!DOCTYPE html>
<html lang="en">
<head>
<meta charset="utf-8">
<title>Saltbush Ledger Partners – Directory Ad</title>
<link rel="stylesheet" href="https://fonts.googleapis.com/css2?family=Crimson+Text&family=Merriweather:wght@900&family=Carlito:wght@700&family=Merriweather+Sans:wght@700&family=Libre+Baskerville&family=Tinos:wght@700&display=swap">
<style>
  :root {
    --yellow: #ffff00;
    --red: #e40000;
    --white: #ffffff;
    --slate: #2f4a4a;
    --ink: #000000;
    --dot: #ff1a1a;
  }
  * { margin: 0; padding: 0; box-sizing: border-box; }
  html, body { width: 1200px; height: 720px; overflow: hidden; background: var(--white); }
  .ad { position: relative; width: 1200px; height: 720px; background: var(--white); }

  .category {
    position: absolute; left: 0; top: 0; width: 1200px; height: 30px;
    background: var(--yellow);
    font: 700 23px/30px "Merriweather Sans", sans-serif;
    color: var(--ink); padding-left: 6px;
  }

  .masthead {
    position: absolute; left: 0; top: 38px; width: 1200px; height: 144px;
    background: var(--red); color: var(--white); text-align: center;
  }
  .firm-name {
    font: 400 80px/1 "Crimson Text", serif;
    padding-top: 10px; letter-spacing: 1px;
  }
  .licence {
    font: 400 20px/1 "Crimson Text", serif;
    margin-top: 22px; letter-spacing: 0.5px;
  }

  .tagline {
    position: absolute; left: 0; top: 182px; width: 1200px; height: 94px;
    text-align: center; color: var(--red);
    font: 900 46px/94px "Merriweather", serif; word-spacing: 4px;
  }

  .services-panel {
    position: absolute; left: 0; top: 276px; width: 1200px; height: 382px;
    background: var(--slate); color: var(--white);
  }
  .intro {
    text-align: center; font: 700 51px/1 "Carlito", sans-serif;
    margin-top: 46px;
  }
  .services { list-style: none; text-align: center; margin-top: 2px; }
  .services li {
    display: inline-block; font: 700 32px/48px "Merriweather Sans", sans-serif;
    letter-spacing: 0.9px; margin: 0 3px;
  }
  .services li::before {
    content: ""; display: inline-block; width: 8px; height: 8px;
    border-radius: 50%; background: var(--dot);
    vertical-align: middle; margin: 0 3px 8px 0;
  }
  .rule {
    position: absolute; left: 58px; top: 250px; width: 1086px; height: 4px;
    background: var(--white);
  }
  .address, .contact {
    position: absolute; top: 264px;
    font: 400 25px/39px "Libre Baskerville", serif; color: var(--white);
    letter-spacing: 0.8px;
  }
  .address { left: 62px; }
  .contact { right: 56px; text-align: right; }

  .web {
    position: absolute; left: 0; top: 658px; width: 1200px; height: 62px;
    background: var(--red); color: var(--white); text-align: center;
    font: 700 36px/64px "Tinos", serif; letter-spacing: 1px;
  }
</style>
</head>
<body>
<main class="ad">
  <div class="category">Accountants</div>

  <header class="masthead">
    <h1 class="firm-name">Saltbush Ledger Partners</h1>
    <p class="licence">Australian Credit Licence 402 918</p>
  </header>

  <p class="tagline">Coastal Insight Second to None</p>

  <section class="services-panel">
    <h2 class="intro">We are here for you all year round to assist with...</h2>
    <ul class="services">
      <li>Accounting &amp; Taxation</li>
      <li>Business Advice</li>
      <li>GST And BAS’s</li><br>
      <li>Mortgage Broking</li>
      <li>Loan Structuring</li><br>
      <li>Self Managed Super Funds</li>
    </ul>
    <div class="rule"></div>
    <address class="address">
      Shop 5 Harbour Walk<br>
      12 Marlin St Kestrel Bay<br>
      PO Box 410 Kestrel Bay 6790
    </address>
    <p class="contact">
      desk@saltbushledger.au<br>
      Ph: 9100 4821<br>
      Fax: 9100 4822
    </p>
  </section>

  <footer class="web">www.saltbushledger.au</footer>
</main>
</body>
</html>
```